The Juniper Coach

I am a life coach specializing in helping people with depression and bipolar disorder. I would like a nice, fun design for a business card.

```html
<!DOCTYPE html>
<html lang="en">
<head>
<meta charset="utf-8">
<title>The Juniper Coach — Business Cards</title>
<link rel="stylesheet" href="https://fonts.googleapis.com/css2?family=Open+Sans:wght@400;600&display=swap">
<style>
  :root {
    --backdrop: #ece8e1;
    --card-white: #f7f7f5;
    --card-yellow: #e8c21c;
    --ink: #4a4a4a;
    --ink-dark: #3a3a3a;
    --accent: #e9b913;
  }
  * { box-sizing: border-box; margin: 0; padding: 0; }
  html, body {
    width: 1200px; height: 942px; overflow: hidden;
    background: var(--backdrop);
    font-family: "Open Sans", Arial, sans-serif;
  }
  .stage {
    width: 1200px; height: 942px;
    display: flex; align-items: center; justify-content: center; gap: 40px;
  }
  .card {
    position: relative;
    width: 540px; height: 309px;
    border-radius: 3px;
    box-shadow: 0 8px 24px rgba(0,0,0,.18);
  }
  .card--front { background: var(--card-white); }
  .card--back  { background: var(--card-yellow); }

  .brand {
    display: flex; align-items: center; gap: 10px;
    font-weight: 400; white-space: nowrap; line-height: 1;
  }
  .brand__dot { border-radius: 50%; flex: none; }

  .card--front .brand {
    position: absolute; left: 250px; top: 48px;
    font-size: 28px; color: var(--ink);
  }
  .card--front .brand__dot { width: 20px; height: 20px; background: var(--accent); }

  .identity { position: absolute; left: 250px; top: 118px; }
  .identity__name { font-size: 30px; color: var(--ink); line-height: 1.1; }
  .identity__title { font-size: 17px; color: var(--accent); margin-top: 2px; }

  .contacts {
    position: absolute; left: 40px; bottom: 40px;
    list-style: none; font-size: 15px; color: var(--ink);
  }
  .contacts li { display: flex; align-items: center; gap: 10px; margin-top: 12px; }
  .contacts svg { width: 16px; height: 16px; flex: none; }

  .card--back .brand {
    position: absolute; left: 0; right: 0; top: 118px; justify-content: center;
    font-size: 38px; color: var(--ink-dark);
  }
  .card--back .brand__dot { width: 26px; height: 26px; background: var(--ink-dark); }
  .website {
    position: absolute; left: 0; right: 0; top: 196px; text-align: center;
    font-size: 14px; letter-spacing: .22em; color: var(--ink);
  }
</style>
</head>
<body>
<main class="stage">
  <section class="card card--front" aria-label="Business card front">
    <div class="brand"><span class="brand__dot"></span><span class="brand__name">The Juniper Coach</span></div>
    <div class="identity">
      <p class="identity__name">Your Name</p>
      <p class="identity__title">Job Title</p>
    </div>
    <ul class="contacts">
      <li>
        <svg viewBox="0 0 16 16" aria-hidden="true"><path d="M4 1 L6.5 4 L5 6 Q6.5 9.5 10 11 L12 9.5 L15 12 L13 15 Q3 13 1 3 Z" fill="var(--accent)"/></svg>
        <span>(310) 555-5555</span>
      </li>
      <li>
        <svg viewBox="0 0 16 16" aria-hidden="true"><rect x="1" y="3" width="14" height="10" fill="var(--accent)"/><path d="M1 3 L8 9 L15 3" fill="none" stroke="#fff" stroke-width="1.3"/></svg>
        <span>youremail@xyz.com</span>
      </li>
    </ul>
  </section>

  <section class="card card--back" aria-label="Business card back">
    <div class="brand"><span class="brand__dot"></span><span class="brand__name">The Juniper Coach</span></div>
    <p class="website">yourwebsite.com</p>
  </section>
</main>
</body>
</html>
```